Poster of Core Values & Motto

Create our core values poster and motto. Attached are our core values and our Motto. This poster represents both of our companies Tidy Pulp & CuraBinix.

Target Market(s)

Our team / employees

Industry/Entity Type

Shredding and Medical Waste

Colors
59FF00
82FF00
B8FF75
E3FFCB
F4FFEA
EB3D1F
EC4F4E
F09395
F8D3D4
FCEDEE

Requirements
Must have
• Include both companies logos

```html
<!DOCTYPE html>
<html lang="en">
<head>
<meta charset="utf-8">
<title>Core Values Poster – Tidy Pulp &amp; CuraBinix</title>
<link rel="stylesheet" href="https://fonts.googleapis.com/css2?family=Poppins:wght@600;700;800&family=Quicksand:wght@500;600&display=swap">
<style>
  :root {
    --backdrop: #263238;
    --paper: #ffffff;
    --green: #0e652e;
    --blue: #1a9fc6;
    --red: #f90c0c;
    --orange: #f76a12;
    --magenta: #b8125e;
    --yellow: #f5bd10;
    --navy: #17375e;
    --brand-red: #d9161c;
    --brand-green: #1f8a3e;
  }
  html, body {
    margin: 0;
    width: 988px;
    height: 1200px;
    overflow: hidden;
    background: var(--backdrop);
  }
  .poster {
    position: absolute;
    left: 180px;
    top: 128px;
    width: 629px;
    height: 944px;
    display: block;
  }
  .head-text { font-family: "Poppins", sans-serif; font-weight: 800; fill: var(--paper); }
  .value-title { font-family: "Poppins", sans-serif; font-weight: 800; font-size: 42px; fill: var(--paper); }
  .value-body { font-family: "Quicksand", sans-serif; font-weight: 500; font-size: 24px; fill: var(--paper); }
  .value-title.on-yellow, .value-body.on-yellow { fill: var(--navy); }
  .motto-label { font-family: "Poppins", sans-serif; font-weight: 700; font-size: 18px; letter-spacing: 4px; fill: var(--navy); }
  .motto-rule { stroke: var(--navy); stroke-width: 2; stroke-dasharray: 7 5; }
  .motto { font-family: "Poppins", sans-serif; font-weight: 800; fill: var(--navy); }
  .gap { stroke: var(--paper); stroke-width: 38; }
  .icon-slot { opacity: 0.28; }
  .brand { font-family: "Poppins", sans-serif; font-weight: 700; }
  .brand-cura { fill: var(--brand-red); }
  .brand-tidy { fill: var(--brand-green); }
</style>
</head>
<body>
<svg class="poster" viewBox="316 225 1106 1659" xmlns="http://www.w3.org/2000/svg" aria-label="Core values poster">
  <rect x="316" y="225" width="1106" height="1659" fill="var(--paper)"/>

  <g class="header">
    <polygon points="316,225 1422,225 1422,475 673,697 316,500" fill="var(--green)"/>
    <polygon points="443,397 743,225 985,225" fill="var(--paper)"/>
    <text class="head-text" x="497" y="536" font-size="155" textLength="480" lengthAdjust="spacingAndGlyphs" transform="rotate(-15.6 497 536)">CORE</text>
    <text class="head-text" x="565" y="725" font-size="235" textLength="830" lengthAdjust="spacingAndGlyphs" transform="rotate(-16.3 565 725)">VALUES</text>
  </g>

  <g class="wheel">
    <path class="segment excellence" fill="var(--blue)" d="M1305.3,1009.5 A505,505 0 0 0 868,757 L868,1007 A255,255 0 0 1 946.8,1019.5 L968,1088.8 L1038.6,1072.5 A255,255 0 0 1 1088.8,1134.5 Z"/>
    <path class="segment teamwork" fill="var(--green)" d="M868,757 A505,505 0 0 0 430.7,1009.5 L647.2,1134.5 A255,255 0 0 1 697.4,1072.5 L768,1088.8 L789.2,1019.5 A255,255 0 0 1 868,1007 Z"/>
    <path class="segment efficient" fill="var(--yellow)" d="M430.7,1009.5 A505,505 0 0 0 430.7,1514.5 L647.2,1389.5 A255,255 0 0 1 618.6,1315 L668,1262 L618.6,1209 A255,255 0 0 1 647.2,1134.5 Z"/>
    <path class="segment secure" fill="var(--magenta)" d="M430.7,1514.5 A505,505 0 0 0 868,1767 L868,1517 A255,255 0 0 1 789.2,1504.5 L768,1435.2 L697.4,1451.5 A255,255 0 0 1 647.2,1389.5 Z"/>
    <path class="segment dependable" fill="var(--orange)" d="M868,1767 A505,505 0 0 0 1305.3,1514.5 L1088.8,1389.5 A255,255 0 0 1 1038.6,1451.5 L968,1435.2 L946.8,1504.5 A255,255 0 0 1 868,1517 Z"/>
    <path class="segment integrity" fill="var(--red)" d="M1305.3,1514.5 A505,505 0 0 0 1305.3,1009.5 L1088.8,1134.5 A255,255 0 0 1 1117.4,1209 L1068,1262 L1117.4,1315 A255,255 0 0 1 1088.8,1389.5 Z"/>

    <line class="gap" x1="868" y1="740" x2="868" y2="1784"/>
    <line class="gap" x1="1318.3" y1="1002" x2="417.7" y2="1522"/>
    <line class="gap" x1="417.7" y1="1002" x2="1318.3" y2="1522"/>

    <rect class="icon-slot" x="695" y="795" width="145" height="110" rx="20" fill="#063d1b" role="img" aria-label="Line icon of two hands clasped in teamwork"/>
    <rect class="icon-slot" x="900" y="795" width="150" height="115" rx="20" fill="#0d6f8f" role="img" aria-label="Line icon of a cheering figure rising from a gift bag"/>
    <rect class="icon-slot" x="1185" y="1100" width="155" height="120" rx="20" fill="#a50606" role="img" aria-label="Line icon of a raised hand beside a heart"/>
    <rect class="icon-slot" x="425" y="1108" width="130" height="132" rx="20" fill="#b5860a" role="img" aria-label="Line icon of a clock set in a gear"/>
    <rect class="icon-slot" x="512" y="1480" width="100" height="132" rx="20" fill="#ff4aa0" role="img" aria-label="Line icon of a hand holding a shield with a tick"/>
    <rect class="icon-slot" x="1025" y="1455" width="125" height="128" rx="20" fill="#b24507" role="img" aria-label="Line icon of a person working at a laptop"/>

    <g class="value teamwork">
      <text class="value-title" x="537" y="945" textLength="213" lengthAdjust="spacingAndGlyphs">SYNERGY /</text>
      <text class="value-title" x="537" y="984" textLength="248" lengthAdjust="spacingAndGlyphs">TEAMWORK</text>
      <text class="value-body" x="537" y="1009" textLength="271" lengthAdjust="spacingAndGlyphs">Get it done attitude with</text>
      <text class="value-body" x="537" y="1035" textLength="211" lengthAdjust="spacingAndGlyphs">humble confidence</text>
    </g>
    <g class="value excellence">
      <text class="value-title" x="945" y="958" textLength="255" lengthAdjust="spacingAndGlyphs">EXCELLENCE</text>
      <text class="value-body" x="945" y="983" textLength="232" lengthAdjust="spacingAndGlyphs">Exceed expectations</text>
      <text class="value-body" x="945" y="1009" textLength="128" lengthAdjust="spacingAndGlyphs">with a smile</text>
    </g>
    <g class="value efficient" text-anchor="middle">
      <text class="value-title on-yellow" x="493" y="1297" textLength="197" lengthAdjust="spacingAndGlyphs">EFFICIENT</text>
      <text class="value-body on-yellow" x="493" y="1322" textLength="192" lengthAdjust="spacingAndGlyphs">on-time, sense of</text>
      <text class="value-body on-yellow" x="493" y="1348" textLength="176" lengthAdjust="spacingAndGlyphs">urgency, always</text>
      <text class="value-body on-yellow" x="493" y="1374" textLength="188" lengthAdjust="spacingAndGlyphs">trying to improve</text>
    </g>
    <g class="value integrity" text-anchor="middle">
      <text class="value-title" x="1246" y="1271" textLength="190" lengthAdjust="spacingAndGlyphs">HONESTY</text>
      <text class="value-title" x="1246" y="1310" textLength="207" lengthAdjust="spacingAndGlyphs">INTEGRITY</text>
      <text class="value-body" x="1246" y="1336" textLength="190" lengthAdjust="spacingAndGlyphs">Do the right thing</text>
    </g>
    <g class="value secure" text-anchor="end">
      <text class="value-title" x="828" y="1578" textLength="204" lengthAdjust="spacingAndGlyphs">SAFE AND</text>
      <text class="value-title" x="828" y="1617" textLength="158" lengthAdjust="spacingAndGlyphs">SECURE</text>
      <text class="value-body" x="828" y="1642" textLength="234" lengthAdjust="spacingAndGlyphs">We are just as secure</text>
      <text class="value-body" x="828" y="1668" textLength="218" lengthAdjust="spacingAndGlyphs">as an armored truck</text>
      <text class="value-body" x="828" y="1694" textLength="127" lengthAdjust="spacingAndGlyphs">with money</text>
    </g>
    <g class="value dependable">
      <text class="value-title" x="924" y="1634" textLength="258" lengthAdjust="spacingAndGlyphs">DEPENDABLE</text>
      <text class="value-body" x="924" y="1660" textLength="180" lengthAdjust="spacingAndGlyphs">Do what you say</text>
      <text class="value-body" x="924" y="1686" textLength="118" lengthAdjust="spacingAndGlyphs">you will do</text>
    </g>

    <g class="motto-block" text-anchor="middle">
      <line class="motto-rule" x1="705" y1="1168" x2="820" y2="1168"/>
      <line class="motto-rule" x1="917" y1="1168" x2="1030" y2="1168"/>
      <text class="motto-label" x="870" y="1175">MOTTO</text>
      <text class="motto" x="868" y="1220" font-size="40" textLength="300" lengthAdjust="spacingAndGlyphs">REMIND PEOPLE</text>
      <text class="motto" x="868" y="1270" font-size="60" textLength="358" lengthAdjust="spacingAndGlyphs">WHAT GREAT</text>
      <text class="motto" x="863" y="1332" font-size="84" textLength="331" lengthAdjust="spacingAndGlyphs">SERVICE</text>
      <text class="motto" x="866" y="1368" font-size="40" textLength="217" lengthAdjust="spacingAndGlyphs">LOOKS LIKE</text>
    </g>
  </g>

  <g class="brands">
    <text class="brand brand-cura" x="375" y="1834" font-size="44" textLength="330" lengthAdjust="spacingAndGlyphs">CuraBinix</text>
    <circle cx="1112" cy="1800" r="38" fill="var(--brand-green)"/>
    <text class="brand brand-tidy" x="1162" y="1816" font-size="48" textLength="220" lengthAdjust="spacingAndGlyphs">Tidy Pulp</text>
  </g>
</svg>
</body>
</html>
```